Play on Words (French Puns)

Cover (11 x 17.8 cm) for a book of French plays on words. (Author: "Mathis Doreau" Title: "The Tumblers" Subtitle "Letter Puzzles To Nibble" Publisher (at the bottom of the page): "Quill Editions"

Target Market(s)

General public

Industry/Entity Type

Book Publisher

Colors

Designer to choose colors to be used in the design.

Requirements
Must have
• "Unserious" look
Should not have
• Eiffel Tower, triumphal arch (it's a book on French language, not on France)

```html
<!DOCTYPE html>
<html lang="en">
<head>
<meta charset="utf-8">
<title>The Tumblers — Mathis Doreau</title>
<link rel="stylesheet" href="https://fonts.googleapis.com/css2?family=Comic+Neue:wght@400;700&family=Luckiest+Guy&display=swap">
<style>
  :root {
    --paper: #ffffff;
    --ink: #1c1c1c;
    --red: #e8414f;
    --green: #7cc242;
    --orange: #f28a1e;
    --purple: #9b5fb8;
    --blue: #2f9fe0;
    --yellow: #f6c21a;
    --teal: #35b6c8;
  }
  * { margin: 0; padding: 0; box-sizing: border-box; }
  html, body { width: 742px; height: 1200px; overflow: hidden; background: var(--paper); }
  .cover {
    position: relative;
    width: 742px;
    height: 1200px;
    background: var(--paper);
    font-family: "Comic Neue", "Comic Sans MS", cursive;
    color: var(--ink);
  }
  .author {
    position: absolute;
    top: 42px;
    width: 100%;
    text-align: center;
    font-weight: 700;
    font-size: 60px;
    letter-spacing: 1px;
  }
  .title {
    position: absolute;
    left: 0;
    width: 100%;
    font-family: "Luckiest Guy", "Comic Neue", cursive;
    font-weight: 400;
  }
  .title-line {
    display: flex;
    justify-content: center;
    line-height: 1;
  }
  .title-line--top { position: absolute; top: 385px; width: 100%; font-size: 112px; gap: 4px; }
  .title-line--bottom { position: absolute; top: 512px; width: 100%; font-size: 104px; gap: 2px; }
  .letter { display: inline-block; }
  .letter:nth-child(odd) { transform: rotate(-4deg); }
  .letter:nth-child(even) { transform: rotate(3deg) translateY(4px); }
  .c-red { color: var(--red); }
  .c-green { color: var(--green); }
  .c-orange { color: var(--orange); }
  .c-purple { color: var(--purple); }
  .c-blue { color: var(--blue); }
  .c-yellow { color: var(--yellow); }
  .c-teal { color: var(--teal); }
  .subtitle {
    position: absolute;
    top: 680px;
    width: 100%;
    text-align: center;
    font-weight: 400;
    font-size: 50px;
  }
  .subtitle-stroke {
    position: absolute;
    left: 218px;
    top: 760px;
    width: 196px;
    height: 36px;
  }
  .publisher {
    position: absolute;
    bottom: 44px;
    width: 100%;
    text-align: center;
    font-size: 26px;
  }
</style>
</head>
<body>
  <main class="cover">
    <h2 class="author">Mathis Doreau</h2>
    <h1 class="title" aria-label="The Tumblers">
      <span class="title-line title-line--top" aria-hidden="true">
        <span class="letter c-red">T</span><span class="letter c-green">H</span><span class="letter c-orange">E</span>
      </span>
      <span class="title-line title-line--bottom" aria-hidden="true">
        <span class="letter c-purple">T</span><span class="letter c-orange">U</span><span class="letter c-blue">M</span><span class="letter c-green">B</span><span class="letter c-yellow">L</span><span class="letter c-red">E</span><span class="letter c-orange">R</span><span class="letter c-teal">S</span>
      </span>
    </h1>
    <p class="subtitle">Letter Puzzles To Nibble</p>
    <svg class="subtitle-stroke" viewBox="0 0 196 36" aria-hidden="true">
      <path d="M4 10 C50 4 120 4 190 8 L60 20 L150 22 L40 32" fill="none" stroke="var(--ink)" stroke-width="5" stroke-linecap="round" stroke-linejoin="round"/>
    </svg>
    <p class="publisher">Quill Editions</p>
  </main>
</body>
</html>
```